Flyer/email in the style of the front page of a newspaper

I would like a flyer designing that i can primt and also insert into an email. I would like the following headings on the page: Free boards/Free re-brand. Independent family business. Orders completed in 2 working days. Established in 1997. Fitters with 15 years experience

Target Market(s)

business to business

Industry/Entity Type

Real Estate Agent

Requirements
Must have
• newspaper front page

```html
<!DOCTYPE html>
<html lang="en">
<head>
<meta charset="utf-8">
<title>Boardwell – Free Boards / Free Re-Brand</title>
<link rel="stylesheet" href="https://fonts.googleapis.com/css2?family=Anton&family=Oswald:wght@500&family=Source+Serif+4:wght@600&family=Open+Sans:wght@600&display=swap">
<style>
  :root {
    --paper: #ebe7de;
    --paper-dark: #d9d3c6;
    --ink: #1c1a18;
    --navy: #1b1f5c;
    --red: #c8202e;
    --bar: #8c8c8c;
    --rule: #4a4a4a;
    --photo-green: #b9c94a;
    --photo-brick: #b98a6e;
    --photo-sky: #a9bfd6;
    --photo-navy: #4a5170;
  }
  * { margin: 0; padding: 0; box-sizing: border-box; }
  html, body { width: 931px; height: 1200px; overflow: hidden; }
  body {
    position: relative;
    background:
      radial-gradient(ellipse at 20% 30%, rgba(255,255,255,.45), transparent 55%),
      radial-gradient(ellipse at 80% 75%, rgba(255,255,255,.35), transparent 50%),
      radial-gradient(ellipse at 50% 50%, var(--paper) 40%, var(--paper-dark) 100%);
    font-family: "Source Serif 4", Georgia, serif;
    color: var(--ink);
  }
  .abs { position: absolute; }

  .masthead {
    left: 0; width: 931px; top: 40px;
    display: flex; justify-content: center; align-items: center; gap: 18px;
  }
  .masthead-mark { width: 26px; height: 26px; background: var(--navy); }
  .masthead-name {
    font-family: "Anton", Impact, sans-serif;
    font-size: 92px; line-height: 1; color: var(--navy); letter-spacing: 1px;
  }

  .headline { left: 48px; top: 212px; width: 840px; height: 84px; }
  .headline text { font-family: "Anton", Impact, sans-serif; font-size: 86px; fill: var(--ink); }

  .subhead { font-weight: 600; line-height: 1.3; }
  .subhead-left { left: 46px; top: 332px; font-size: 24px; width: 200px; }
  .subhead-right { left: 748px; top: 320px; font-size: 18.5px; width: 140px; line-height: 1.42; }
  .subhead-bottom { left: 48px; top: 908px; font-size: 25px; white-space: nowrap; }

  .bars {
    background: repeating-linear-gradient(to bottom, var(--bar) 0 7px, transparent 7px 17.9px);
  }
  .bars-left { left: 48px; top: 415px; width: 198px; height: 455px; }
  .bars-mid-a { left: 280px; top: 646px; width: 199px; height: 222px; }
  .bars-mid-b { left: 514px; top: 646px; width: 197px; height: 222px; }
  .bars-right { left: 748px; top: 415px; width: 136px; height: 294px; }
  .bars-right-foot { left: 748px; top: 841px; width: 136px; height: 29px; }
  .bars-wide { left: 48px; top: 959px; width: 642px; height: 43px; }
  .bars-col-a { left: 48px; top: 1024px; width: 307px; height: 61px; }
  .bars-col-b { left: 383px; top: 1024px; width: 307px; height: 61px; }

  .photo-main {
    left: 279px; top: 318px; width: 438px; height: 300px;
    background: linear-gradient(135deg, var(--photo-green) 0%, var(--photo-brick) 100%);
  }
  .photo-side {
    left: 748px; top: 709px; width: 136px; height: 124px;
    background: linear-gradient(180deg, var(--photo-sky) 0%, var(--photo-navy) 100%);
  }

  .rule-v { left: 730px; top: 318px; width: 1px; height: 550px; background: var(--rule); }
  .rule-h { left: 48px; top: 893px; width: 836px; height: 1px; background: var(--rule); }

  .phone-box {
    left: 735px; top: 928px; width: 149px; height: 153px;
    border: 1.5px solid #888; background: rgba(0,0,0,.06);
    text-align: center;
  }
  .phone-box svg { display: block; margin: 26px auto 0; }
  .phone-number {
    font-family: "Oswald", "Arial Narrow", sans-serif; font-weight: 500;
    font-size: 22px; line-height: 1; color: var(--navy); margin-top: 18px;
    white-space: nowrap;
  }

  .footer {
    left: 48px; top: 1121px; width: 847px; height: 39px;
    border: 1px solid #555;
    display: flex; align-items: center;
    font-family: "Open Sans", Arial, sans-serif; font-weight: 600; font-size: 14.5px;
    color: var(--ink); white-space: nowrap;
  }
  .footer-label { color: var(--navy); }
  .footer-item { display: flex; align-items: center; gap: 9px; }
  .footer svg { flex: none; }
</style>
</head>
<body>
  <header class="abs masthead">
    <span class="masthead-mark"></span>
    <span class="masthead-name">Boardwell</span>
  </header>

  <svg class="abs headline" viewBox="0 0 840 84" aria-label="Free boards / free re-brand">
    <text x="0" y="80" textLength="840" lengthAdjust="spacingAndGlyphs">FREE BOARDS/FREE RE-BRAND</text>
  </svg>

  <h2 class="abs subhead subhead-left">Independent family business.</h2>
  <div class="abs bars bars-left"></div>

  <div class="abs photo-main" role="img" aria-label="Photo of a For Sale board outside a house"></div>
  <div class="abs bars bars-mid-a"></div>
  <div class="abs bars bars-mid-b"></div>

  <div class="abs rule-v"></div>

  <h2 class="abs subhead subhead-right">Orders completed in 2 working days.</h2>
  <div class="abs bars bars-right"></div>
  <div class="abs photo-side" role="img" aria-label="Photo of a To Let board on a post"></div>
  <div class="abs bars bars-right-foot"></div>

  <div class="abs rule-h"></div>

  <h2 class="abs subhead subhead-bottom">Established in 1997. Fitters with 15 years experience</h2>
  <div class="abs bars bars-wide"></div>
  <div class="abs bars bars-col-a"></div>
  <div class="abs bars bars-col-b"></div>

  <aside class="abs phone-box">
    <svg width="38" height="62" viewBox="0 0 38 62" aria-hidden="true">
      <rect x="4" y="0" width="5" height="12" rx="2" fill="#808080"/>
      <rect x="0" y="10" width="38" height="52" rx="8" fill="#808080"/>
      <rect x="7" y="17" width="24" height="18" rx="3" fill="#d8d4cb"/>
    </svg>
    <div class="phone-number">0333 555 0148</div>
  </aside>

  <footer class="abs footer">
    <span class="footer-label" style="margin-left:30px">Contact Us</span>
    <span class="footer-item" style="margin-left:30px">
      <svg width="22" height="16" viewBox="0 0 22 16" aria-hidden="true">
        <rect x="1" y="1" width="20" height="14" fill="none" stroke="var(--red)" stroke-width="1.8"/>
        <path d="M1 1 L11 9 L21 1 M1 15 L8 8 M21 15 L14 8" fill="none" stroke="var(--red)" stroke-width="1.8"/>
      </svg>
      icon_mail info@boardwell.co.uk
    </span>
    <span class="footer-label" style="margin-left:58px">Learn more</span>
    <span class="footer-item" style="margin-left:28px">
      <svg width="20" height="20" viewBox="0 0 20 20" aria-hidden="true">
        <circle cx="10" cy="10" r="8.5" fill="none" stroke="var(--red)" stroke-width="1.8"/>
        <path d="M1.5 10 H18.5 M10 1.5 C5 6 5 14 10 18.5 M10 1.5 C15 6 15 14 10 18.5" fill="none" stroke="var(--red)" stroke-width="1.5"/>
      </svg>
      www.boardwell.co.uk
    </span>
  </footer>
</body>
</html>
```